Corporate Brochure Design for Cyber Resilience Solution (A4 PDF, 4 pages)

We are looking for a high-calibre designer to create a 4-page A4 PDF brochure promoting our digital resilience solution, Halcrest, and our company, DLO Dunmere Ledger Orbis. The design must reflect a premium, boardroom-ready style, as it is primarily shared with senior leaders in regulated financial services.
DLO Dunmere Ledger Orbis is a strategic advisory firm helping leadership teams achieve digital operational resilience. We combine board-level advisory, executive education, and a proprietary SaaS platform — Halcrest — to deliver cyber governance and compliance at scale.
Website: www.dlorbis.ie
Design Goals:
Target audience: C-level executives, particularly in financial services
Purpose: To instil confidence in our company and solution following an initial meeting
Style: Clean, modern, and corporate premium (5-star quality)
Tone: Strategic and authoritative
Format: A4 PDF (approx. 4 pages)
Visuals: Designer to select from provided Halcrest screenshots and align with overall layout
Continuity: Should visually complement our website and internal reports (Photoshop report templates provided for reference)
Content Provided:
Finalised brochure text (Microsoft Word format)
Logos for DLO and Halcrest
A folder of screenshots from our platform
Two Photoshop files used for internal reports (style inspiration)
Brochure Sections to Design:
Cover Page
Logo, strong visual brand, compelling title or tagline
Executive Summary / Who We Are
Introduce DLO and our flagship platform, Halcrest
What We Offer / How We Work With Clients
Break down our Steady Keel Programme and 4-phase engagement model
Use Cases & Contact
Highlight regulated sector experience and encourage next steps
Visual Direction:
Visual hierarchy must support strategic messaging
Include selected Halcrest platform screenshots where appropriate
Use consistent font and colour palette based on provided templates and site
Clean, uncluttered layout with room to breathe — not dense or technical
Deliverables:
4-page print-ready PDF
Source files (InDesign preferred)
Web-optimised PDF version
Any non-standard fonts or licences used
financial sector senior level

```html
<!DOCTYPE html>
<html lang="en">
<head>
<meta charset="utf-8">
<title>Steady Keel Programme – What We Offer</title>
<link href="https://fonts.googleapis.com/css2?family=Roboto+Condensed:wght@300;400;700&display=swap" rel="stylesheet">
<style>
  :root {
    --red: #e5252a;
    --ink: #3a3a3a;
    --grey: #4a4a4a;
    --paper: #ffffff;
  }
  * { margin: 0; padding: 0; box-sizing: border-box; }
  html, body { width: 848px; height: 1200px; overflow: hidden; background: var(--paper); }
  body {
    position: relative;
    font-family: "Roboto Condensed", "Arial Narrow", sans-serif;
    font-weight: 300;
    color: var(--ink);
  }
  .masthead {
    position: absolute; top: 36px; left: 0; width: 848px; text-align: center;
  }
  .masthead__company {
    font-size: 12px; letter-spacing: 0.32em; color: var(--grey); font-weight: 400;
  }
  .masthead__label {
    margin-top: 12px; font-size: 15px; font-weight: 700; color: var(--red);
    letter-spacing: 0.95em; padding-left: 0.95em;
  }
  .section-title {
    color: var(--red); font-weight: 300; font-size: 27px; letter-spacing: 0.01em;
    line-height: 1;
  }
  .body-text { font-size: 15.6px; line-height: 22.5px; }

  .offer { position: absolute; left: 169px; top: 232px; width: 520px; }
  .offer .body-text { margin-top: 26px; }
  .offer-list { list-style: none; margin-left: 27px; }
  .offer-list li { position: relative; padding-left 0; }
  .offer-list li::before {
    content: ""; position: absolute; left: -17px; top: 8px;
    width: 5px; height: 5px; border-radius: 50%; background: var(--red);
  }

  .process { position: absolute; left: 78px; top: 673px; width: 700px; }
  .process__cols { display: flex; margin-top: 24px; }
  .process__col--left { width: 350px; }
  .process__col--right { width: 330px; padding-top: 22px; margin-left: 0; }
  .phase-list { list-style: none; margin-left: 13px; }
  .phase__name { color: var(--red); display: flex; }
  .phase__num { width: 15px; }
  .phase__desc { padding-left: 15px; }
  .process__note { position: absolute; left: 347px; top: 314px; width: 320px; }

  .folio {
    position: absolute; top: 1121px; left: 0; width: 848px; text-align: center;
    color: var(--red); font-size: 15px; font-weight: 400;
  }
</style>
</head>
<body>
  <header class="masthead">
    <div class="masthead__company">DUNMERE LEDGER ORBIS</div>
    <div class="masthead__label">REPORT</div>
  </header>

  <section class="offer">
    <h2 class="section-title">WHAT WE OFFER</h2>
    <div class="body-text">
      <p>Our Steady Keel Programme helps organisations measure, manage, and continuously improve their cyber resilience posture. Powered by our Halcrest platform and supported by expert advisors, the programme delivers:</p>
      <ul class="offer-list">
        <li>Regulator-grade assessments and reporting</li>
        <li>Strategic alignment with regulatory frameworks</li>
        <li>Embedded vDORO (Virtual Digital Operational Resilience Officer) support</li>
        <li>Customised maturity roadmaps and executive dashboards</li>
        <li>Integration of executive education into our delivery model — clients benefit from strategic enablement through industry-recognised qualifications, hands-on materials, and leadership forums.</li>
        <li>Access to exclusive educational content including certified training programmes, peer forums, and qualifications via the Northlight Cyber Academy.</li>
      </ul>
    </div>
  </section>

  <section class="process">
    <h2 class="section-title">HOW WE WORK WITH CLIENTS</h2>
    <div class="process__cols body-text">
      <div class="process__col--left">
        <p>Our proven four-phase engagement model includes:</p>
        <ol class="phase-list">
          <li class="phase">
            <div class="phase__name"><span class="phase__num">1.</span>Initial Discovery &amp; Baseline Assessment</div>
            <p class="phase__desc">We contextualise your risk posture and identify regulatory and operational exposures.</p>
          </li>
          <li class="phase">
            <div class="phase__name"><span class="phase__num">2.</span>Platform Deployment &amp; Enablement</div>
            <p class="phase__desc">We configure and onboard Halcrest, enabling full visibility and role-specific access.</p>
          </li>
          <li class="phase">
            <div class="phase__name"><span class="phase__num">3.</span>Ongoing Strategic Advisory (vDORO Model)</div>
            <p class="phase__desc">Your dedicated advisor drives governance, compliance alignment, and incident readiness.</p>
          </li>
          <li class="phase">
            <div class="phase__name"><span class="phase__num">4.</span>Maturity Reporting &amp; Board Briefings</div>
            <p class="phase__desc">We provide scheduled, digestible reporting for leadership and regulators.</p>
          </li>
        </ol>
      </div>
      <div class="process__col--right">
        <ol class="phase-list" start="5">
          <li class="phase">
            <div class="phase__name"><span class="phase__num">5.</span>Embedded Executive Education</div>
            <p class="phase__desc">Our engagement doesn’t stop at reports and advisory — we empower clients with ongoing access to the Northlight Cyber Academy’s portfolio of certified training programmes, educational resources, and curated peer forums. This ensures that your leadership and operational teams are continuously upskilled to meet evolving resilience, compliance, and governance expectations.</p>
          </li>
        </ol>
      </div>
    </div>
    <p class="process__note body-text">We provide scheduled, digestible reporting for leadership and regulators.</p>
  </section>

  <div class="folio">9</div>
</body>
</html>
```